Summer Music/Chorus/Choir Camp for Young Singers Ages 8-13

We need a flyer for a summer camp for young singers ages 8-13. We are nonprofit community children's chorus in Miami, FL. Our camp provides specialized training in music theory, sight-reading,and aural training through daily choral rehearsals in an environment that is both positive and a lot of fun! Our camp offers children the opportunity to come as they are, no matter the level of experience, and grow tremendously in their musicianship skills. In addition to this, our campers participate in song-writing, masterclasses, community performances, and media projects. The final design should be clean, fun, not too crowded, should appeal to boys and girls ages 8-13, and something someone that age would consider "cool" and not too childish. Drawings are cool, something different.
Updates

Target Market(s)

Ages 8-13 and parents of those kids.

Industry/Entity Type

Community

Requirements
Must have
• All info attached.
Nice to have
• Things that relate to music, especially related to singing/choirs
Should not have
• instruments, stock photos of children, or photos from our website (unless they are used very creatively), or photos in general. I've attached our previous camp flyer and our current organization flyer but I don't necessarily want this flyer to look like those.

```html
<!DOCTYPE html>
<html lang="en">
<head>
<meta charset="utf-8">
<title>Summer Choral Camp</title>
<link href="https://fonts.googleapis.com/css2?family=Mystery+Quest&family=Shadows+Into+Light&family=Fira+Sans+Condensed:wght@500;600&display=swap" rel="stylesheet">
<style>
:root{
  --sky:#d6eef5;
  --paper:#ede6d6;
  --paper-edge:#c9bca2;
  --ink:#2a2622;
  --pink:#e0307a;
  --lime:#c7e08a;
  --text:#3a3a34;
  --cyan:#34b9e0;
  --green:#8fd16b;
  --purple:#8a4fa8;
  --orange:#f9a61a;
  --note-ink:#4a2a8a;
  --note-back:#5c6fd0;
}
*{margin:0;padding:0;box-sizing:border-box}
html,body{width:834px;height:1200px;overflow:hidden;background:var(--sky)}
.flyer{position:relative;width:834px;height:1200px;background:var(--sky);overflow:hidden}

.ribbons{position:absolute;left:0;top:160px;width:834px;height:900px;
  background:linear-gradient(160deg,rgba(240,120,170,.3),rgba(250,220,90,.25) 30%,rgba(120,200,230,.3) 55%,rgba(150,210,110,.3) 75%,rgba(170,120,210,.3));}

.headphones-art{position:absolute;left:40px;top:18px;width:760px;height:330px;border-radius:170px 170px 30px 30px;
  background:linear-gradient(180deg,#f2f5f7 0%,#c9d1d6 22%,#e86aa8 48%,#e0307a 70%,#f06a3a 100%);}

.title{position:absolute;left:0;top:43px;width:834px;text-align:center;
  font-family:"Mystery Quest",cursive;font-weight:400;font-size:72px;line-height:90px;color:#1c1c1c;letter-spacing:1px;
  text-shadow:0 0 4px #fff,0 0 8px rgba(255,255,255,.8)}

.notebook{position:absolute;left:60px;top:292px;width:700px;height:580px;background:var(--paper);
  border:2px solid var(--paper-edge);box-shadow:0 4px 10px rgba(0,0,0,.25);
  background-image:repeating-linear-gradient(180deg,transparent 0 21px,rgba(150,170,190,.25) 21px 22px),
  linear-gradient(90deg,transparent 348px,rgba(0,0,0,.12) 350px,transparent 354px);}
.copy{position:absolute;left:0;width:696px;text-align:center;white-space:nowrap;
  font-family:"Shadows Into Light",cursive;color:var(--ink);font-size:30px;line-height:36px}
.copy.intro{top:30px;line-height:35px}
.copy.mission{top:134px}
.copy.welcome{top:350px}
.copy.grades{top:430px}
.copy.cta{top:470px;color:var(--pink);font-size:38px;line-height:44px}

.partner-badge{position:absolute;left:114px;top:516px;width:56px;height:56px;background:#3a3a3a;border-radius:2px}
.partner-name{position:absolute;left:262px;top:538px;font-family:"Fira Sans Condensed",sans-serif;font-weight:600;font-size:21px;line-height:28px;color:#1e1e1e;display:flex;align-items:center;gap:8px}
.partner-name .dot{width:14px;height:14px;background:#1e1e1e}
.chorus-name{position:absolute;left:520px;top:522px;width:150px;text-align:center;font-family:"Fira Sans Condensed",sans-serif;font-weight:600;font-size:20px;line-height:24px;color:#7a9aa6}

.info-panel{position:absolute;left:42px;top:878px;width:738px;height:282px;background:var(--lime)}
.info{position:absolute;left:42px;top:878px;width:738px;padding-top:18px;
  font-family:"Fira Sans Condensed",sans-serif;font-weight:500;color:var(--text);text-align:center;font-size:21px;line-height:36px}
.label.loc{color:var(--pink)}
.label.cost{color:var(--cyan)}
.label.phone{color:var(--green)}
.label.email{color:var(--purple)}

.note-back{position:absolute;left:592px;top:990px;width:160px;height:160px;background:var(--note-back);transform:rotate(-4deg)}
.sticky{position:absolute;left:594px;top:990px;width:180px;height:150px;background:var(--orange);
  transform:rotate(-20deg);box-shadow:2px 4px 6px rgba(0,0,0,.25);
  font-family:"Fira Sans Condensed",sans-serif;font-weight:600;color:var(--note-ink);font-size:21px;line-height:30px;text-align:center;padding-top:26px}
.pin{position:absolute;left:600px;top:978px;width:20px;height:20px;border-radius:50%;background:#6f7c86;box-shadow:1px 2px 3px rgba(0,0,0,.3)}
</style>
</head>
<body>
<div class="flyer">
  <div class="ribbons" role="img" aria-label="Colourful flowing music staff ribbons with notes"></div>
  <div class="headphones-art" role="img" aria-label="Large silver headphones with glowing pink speakers framing the title"></div>
  <h1 class="title">SUMMER CHORAL<br>CAMP</h1>

  <section class="notebook">
    <p class="copy intro">"Youth and children who love to sing will have a blast<br>at our choral camp!</p>
    <p class="copy mission">Our music educators and industry<br>professionals are dedicated to enhancing the lives of<br>young singers through choral training which develops<br>vocal technique, ear-training, music reading,<br>and interpersonal skills.</p>
    <p class="copy welcome">Activities are fun and interactive and former music<br>training is not necessary.</p>
    <p class="copy grades">Singers in grades 3-9 are invited to attend!</p>
    <p class="copy cta">Register today!"</p>
    <div class="partner-badge"></div>
    <div class="partner-name"><span class="dot"></span>Lantern Arts Fund</div>
    <div class="chorus-name">Brightsong<br>Youth Chorus</div>
  </section>

  <div class="info-panel"></div>
  <div class="note-back"></div>
  <div class="sticky">"Dates and Times-<br>July 18-29,<br>9am-3pm (M-F)"</div>
  <div class="pin"></div>

  <section class="info">
    <div>Extended hours available (7:30am-5:30pm) for an extra $50 per week.</div>
    <div><span class="label loc">LOCATION</span>- Southbay Community Arts Hall, 4820 SW 180th Avenue</div>
    <div>Miami, FL 33189</div>
    <div><span class="label cost">COST</span>- *$300 for 2-week session</div>
    <div>*Price does not include lunch.</div>
    <div><span class="label phone">PHONE</span>- 305.555.0148</div>
    <div><span class="label email">EMAIL</span>- hello@brightsongchorus.org</div>
  </section>
</div>
</body>
</html>
```